Letter Head Design

I need a letter head design based on my company logo that I attached.
Include phone number: (403)582-4316
Address: 347 14th Avenue NE, Calgary, Alberta, Canada, T3K 4R8

Industry/Entity Type

It Company

```html
<!DOCTYPE html>
<html lang="en">
<head>
<meta charset="utf-8">
<title>Northvale Interiors Corp. — Letterhead</title>
<link href="https://fonts.googleapis.com/css2?family=Source+Sans+3:wght@400;600;700&display=swap" rel="stylesheet">
<style>
  :root {
    --backdrop: #ffffff;
    --paper: #ffffff;
    --heading: #7a7a7a;
    --body: #6a6a6a;
    --ink: #111111;
    --brand-blue: #1a64b4;
    --brand-green: #5bb31f;
    --signature-tone: #2a2a2a;
  }
  * { box-sizing: border-box; margin: 0; padding: 0; }
  html, body {
    width: 1200px; height: 1071px; overflow: hidden;
    background: var(--backdrop);
    font-family: "Source Sans 3", "Helvetica Neue", Arial, sans-serif;
  }
  .sheet {
    position: absolute; left: 328px; top: 150px;
    width: 543px; height: 768px;
    background: var(--paper);
    box-shadow: 0 0 18px rgba(0,0,0,0.12);
  }
  .brand {
    position: absolute; left: 39px; top: 118px;
    display: flex; align-items: center; gap: 6px;
  }
  .brand-square {
    width: 14px; height: 14px; background: var(--brand-green);
  }
  .brand-name {
    font-size: 21px; font-weight: 600; color: var(--brand-blue);
    line-height: 1; letter-spacing: -0.2px;
  }
  .letter-title {
    position: absolute; left: 118px; top: 190px;
    font-size: 13px; font-weight: 700; color: var(--heading);
  }
  .sidebar {
    position: absolute; left: 20px; top: 219px; width: 75px;
    text-align: right; font-size: 8.4px; line-height: 11px; color: var(--ink);
  }
  .sidebar-item { margin-bottom: 7px; }
  .sidebar-item strong { font-weight: 700; display: block; }
  .letter-body {
    position: absolute; left: 118px; top: 218px; width: 373px;
    font-size: 8.45px; line-height: 11.85px; color: var(--body);
  }
  .letter-body p { margin-bottom: 11.85px; }
  .sign-off {
    position: absolute; left: 118px; top: 562px;
    font-size: 8.4px; color: var(--body);
  }
  .signature {
    position: absolute; left: 116px; top: 570px;
    width: 162px; height: 26px;
    background: linear-gradient(90deg, rgba(42,42,42,0.18), rgba(42,42,42,0.08));
    border-radius: 3px;
  }
  .footer {
    position: absolute; left: 39px; top: 715px;
    font-size: 8.4px; line-height: 11.5px; color: var(--body);
  }
  .footer strong { font-weight: 700; color: #444; }
</style>
</head>
<body>
  <main class="sheet">
    <header class="brand">
      <span class="brand-square" aria-hidden="true"></span>
      <span class="brand-name">Northvale Interiors</span>
    </header>

    <h1 class="letter-title">Lorem ipsum</h1>

    <aside class="sidebar">
      <div class="sidebar-item"><strong>Lorem ipsum</strong>dolor sit amet.</div>
      <div class="sidebar-item"><strong>Lorem</strong>ipsum dolor sit</div>
      <div class="sidebar-item"><strong>Lorem</strong>ipsum</div>
    </aside>

    <section class="letter-body">
      <p>Dolor sit amet, consectetur adipiscing elit. Morbi ut ipsum sit amet ipsum sodales venenatis at et arcu. Sed feugiat enim vitae bibendum condimentum. Aliquam vel mattis mauris. Aliquam nec dolor at neque rhoncus aliquam. Nam fringilla condimentum lacus, et posuere purus imperdiet ac. Suspendisse nisl eros, rhoncus a vestibulum vitae, fringilla in sem. Cras nec mauris nec leo viverra euismod in vel odio. In pellentesque dolor eu nunc tincidunt mollis. Mauris dignissim lectus at mauris egestas, in pharetra nisi hendrerit. Aenean sit amet ante sollicitudin, facilisis orci sit amet, dictum dolor. Nullam bibendum feugiat turpis, vitae aliquet nisi porttitor id. Vivamus erat lorem, imperdiet sed nulla sodales, sagittis lacinia urna. In a tristique felis. Ut dui diam, rhoncus eget gravida sit amet, convallis at eros. Integer cursus nec sem et lacinia.</p>
      <p>Nunc ligula odio, iaculis at ante eget, tincidunt adipiscing ante. Vestibulum mattis sapien dolor, porta porttitor urna dapibus sed. Nunc egestas ipsum et arcu fermentum, eget vulputate nunc semper. Ut volutpat venenatis porttitor. Proin accumsan cursus nisl et condimentum. Praesent tempus sapien quis augue feugiat, vitae auctor risus scelerisque. Nulla vehicula, dui in commodo lobortis, massa mi convallis mi, sit amet pellentesque ligula lorem at erat. Praesent porttitor lectus quis felis consectetur, id auctor dolor commodo. Curabitur dictum, libero in aliquam tincidunt, nunc tellus pretium tellus, sed facilisis magna dui at eros. Ut at orci aliquam, tincidunt nibh interdum, auctor ipsum. Ut molestie orci nec lectus vehicula vestibulum.</p>
      <p>Maecenas accumsan, augue et luctus semper, massa nulla fermentum est, ac dictum tellus lacus in erat. Aliquam tristique, augue et tristique ultricies, dui urna commodo justo, id convallis purus magna quis urna. Class aptent taciti sociosqu ad litora torquent per conubia nostra, per inceptos himenaeos. Vestibulum quis nibh nec arcu fringilla sollicitudin sed nec odio. Vestibulum adipiscing ligula sit amet lorem iaculis, quis venenatis turpis rhoncus. Praesent vitae pellentesque odio. Phasellus at magna luctus risus consectetur lobortis. Aliquam ac ultricies lorem, eget lobortis ante. Donec et nisl et sem ultrices hendrerit. In ullamcorper vitae enim non auctor. Fusce pharetra magna nec nisi laoreet iaculis. Phasellus rutrum lorem in leo dictum hendrerit. Praesent a mauris nec eros tempor facilisis.</p>
    </section>

    <div class="sign-off">Fusce scelerisque</div>
    <div class="signature" role="img" aria-label="Handwritten signature"></div>

    <footer class="footer">
      347 14th Avenue NE, Calgary, Alberta, Canada, T3K 4R8<br>
      <strong>phone</strong>: (403)582-4316
    </footer>
  </main>
</body>
</html>
```